Zelmiroo Pop Up design for zelmiroo.com website to collect customer data

I want a pop up designed for my site zelmiroo.com. It is for signup to the site itself. I want to give my users some value in order to sign up. I want this to have graphics and to collect their full name, email address, country they are from. It must say Sign up today and receive all these items for free, A $129 Value, 1. Zelmiroo Custom Travel tools on Web App, The Ebook Packing Light for Long Journeys, and the Golden Route Planner Sheets!

I want this to look exciting so people actually sign up.
I want to be able to put this on facebook and add to my wordpress website.
I want it to match my current website
I currently use ninja forms on my site

Once designed this also needs to be coded for my site.
You can get my color scheme right on the site. I want this to pop

thanks

Industry/Entity Type

Travel

Font styles to use
Serif
Sans Serif

Colors
33a6d7
9bcb3c
ffffff

Requirements
Must have
• A graphic of the ebook, an arrow rounded or something bringing attention to the free items. A sign up point asking for first name, last name, email. I use ninja forms and mailchimp. this will be a pop up within all of my blogs and every page of my site, also country

```html
<!DOCTYPE html>
<html lang="en">
<head>
<meta charset="utf-8">
<title>Zelmiroo Sign Up</title>
<link rel="stylesheet" href="https://fonts.googleapis.com/css2?family=Lato:wght@400;700&display=swap">
<style>
  :root {
    --blue: #33a6d7;
    --button-blue: #2a9bd8;
    --green: #9bcb3c;
    --white: #ffffff;
    --ink: #3a3a3a;
    --muted: #8a8a8a;
    --field-line: #9a9a9a;
    --site-header: #5a5a5a;
    --site-dim-top: #3f5a35;
    --site-dim-bottom: #2f3a28;
    --social-dim: #4d6a1e;
    --chat-dim: #8a4a22;
  }
  * { box-sizing: border-box; margin: 0; padding: 0; }
  html, body { width: 1200px; height: 675px; overflow: hidden; }
  body { font-family: "Lato", Arial, sans-serif; position: relative; background: var(--site-dim-bottom); }

  .site-backdrop { position: absolute; inset: 0; }
  .site-header { position: absolute; left: 0; top: 0; width: 1200px; height: 124px; background: var(--site-header); }
  .site-hero {
    position: absolute; left: 0; top: 124px; width: 1200px; height: 551px;
    background: linear-gradient(180deg, var(--site-dim-top) 0%, #4a5e3a 45%, var(--site-dim-bottom) 100%);
  }
  .site-brand-dot { position: absolute; left: 150px; top: 4px; width: 76px; height: 76px; border-radius: 50%; background: #1e4f6e; }
  .site-social { position: absolute; top: 26px; left: 819px; display: flex; gap: 10px; }
  .site-social span { width: 30px; height: 30px; border-radius: 50%; background: var(--social-dim); }
  .site-chat {
    position: absolute; left: 1113px; top: 608px; width: 54px; height: 54px;
    border-radius: 50%; background: var(--chat-dim);
    display: flex; align-items: center; justify-content: center;
  }

  .signup-popup { position: absolute; left: 72px; top: 43px; width: 1054px; height: 594px; display: flex; }
  .popup-photo {
    width: 658px; height: 594px;
    background: linear-gradient(160deg, #3f6e2a 0%, #4d7a35 30%, #5b5650 55%, #3d4a3c 80%, #2f5a26 100%);
  }
  .popup-side { width: 396px; height: 594px; display: flex; flex-direction: column; }

  .signup-form { height: 290px; background: var(--white); position: relative; }
  .signup-title { position: absolute; left: 44px; top: 32px; font-size: 19px; font-weight: 400; color: var(--ink); }
  .field { position: absolute; border-bottom: 2px solid var(--field-line); font-size: 12px; color: var(--muted); padding-bottom: 4px; }
  .field-name { left: 44px; top: 106px; width: 145px; }
  .field-email { left: 207px; top: 106px; width: 145px; }
  .field-country { left: 44px; top: 168px; width: 308px; }
  .signup-button {
    position: absolute; left: 46px; top: 230px; width: 107px; height: 27px;
    border-radius: 14px; background: var(--button-blue); color: var(--white);
    font-size: 12px; display: flex; align-items: center; justify-content: center;
  }

  .free-items { flex: 1; background: var(--green); position: relative; color: var(--white); }
  .free-heading { position: absolute; left: 44px; top: 20px; width: 340px; font-size: 18.5px; line-height: 27px; font-weight: 400; }
  .free-heading .free-word { color: var(--blue); font-size: 25px; }
  .item { position: absolute; width: 150px; text-align: center; font-size: 12px; line-height: 14.5px; color: #3f4a2a; }
  .item-icon {
    width: 52px; height: 52px; border-radius: 50%; background: var(--white);
    margin: 0 auto 8px; display: flex; align-items: center; justify-content: center;
  }
  .item-value { left: 41px; top: 92px; }
  .item-planner { left: 182px; top: 92px; }
  .item-ebook { left: 41px; top: 180px; }
  .item-tools { left: 186px; top: 180px; }
</style>
</head>
<body>
  <div class="site-backdrop">
    <div class="site-header"></div>
    <div class="site-hero" role="img" aria-label="Dimmed website hero photo of a green mountain landscape"></div>
    <div class="site-brand-dot"></div>
    <div class="site-social"><span></span><span></span><span></span><span></span><span></span><span></span><span></span></div>
    <div class="site-chat">
      <svg width="22" height="20" viewBox="0 0 22 20"><path d="M2 2h18v12H9l-5 4v-4H2z" fill="#c9a58a"/></svg>
    </div>
  </div>

  <div class="signup-popup">
    <div class="popup-photo" role="img" aria-label="Aerial photo of tall waterfalls cascading down a rocky gorge surrounded by rainforest"></div>
    <div class="popup-side">
      <div class="signup-form">
        <h2 class="signup-title">Sign Up</h2>
        <div class="field field-name">Full Name</div>
        <div class="field field-email">Email</div>
        <div class="field field-country">Country Name</div>
        <div class="signup-button">Sign Up</div>
      </div>
      <div class="free-items">
        <p class="free-heading">Sign Up Today And Receive All These Items For <span class="free-word">Free...!!!</span></p>

        <div class="item item-value">
          <div class="item-icon">
            <svg width="32" height="32" viewBox="0 0 32 32" fill="none" stroke="#9bcb3c" stroke-width="1.6">
              <ellipse cx="11" cy="9" rx="7" ry="2.5"/><path d="M4 9v4c0 1.4 3 2.5 7 2.5M4 13v4c0 1.4 3 2.5 7 2.5M4 17v4c0 1.4 3 2.5 7 2.5M18 9v3"/>
              <circle cx="21" cy="20" r="7"/><path d="M23 17.5h-3a1.2 1.2 0 0 0 0 2.5h2a1.2 1.2 0 0 1 0 2.5h-3M21 16v1.5M21 22.5V24"/>
            </svg>
          </div>
          $129 Value
        </div>

        <div class="item item-planner">
          <div class="item-icon">
            <svg width="30" height="32" viewBox="0 0 30 32" fill="none" stroke="#9bcb3c" stroke-width="1.6">
              <rect x="5" y="5" width="20" height="24" rx="1"/><rect x="10" y="2" width="10" height="5" rx="1"/>
              <path d="M9 13l1.5 1.5L13 12M9 19l1.5 1.5L13 18M9 25l1.5 1.5L13 24M16 13h6M16 19h6M16 25h6"/>
            </svg>
          </div>
          Golden Route Planner Sheets
        </div>

        <div class="item item-ebook">
          <div class="item-icon">
            <svg width="32" height="32" viewBox="0 0 32 32" fill="none" stroke="#9bcb3c" stroke-width="1.6">
              <rect x="4" y="4" width="18" height="25" rx="2"/><rect x="7" y="8" width="12" height="15"/>
              <rect x="18" y="10" width="10" height="14" rx="1"/><path d="M9 12h8M9 15h8M9 18h5M20 14h6M20 17h6M20 20h4"/>
            </svg>
          </div>
          The Ebook<br>Packing Light for<br>Long Journeys
        </div>

        <div class="item item-tools">
          <div class="item-icon">
            <svg width="32" height="32" viewBox="0 0 32 32" fill="none" stroke="#9bcb3c" stroke-width="1.6">
              <rect x="3" y="9" width="22" height="16" rx="2"/><path d="M10 9V6h8v3M3 15h22"/>
              <circle cx="24" cy="23" r="6" fill="#ffffff"/><path d="M24 20v3l2 1.5"/>
            </svg>
          </div>
          Zelmiroo Custom<br>Travel tools on<br>Web App
        </div>
      </div>
    </div>
  </div>
</body>
</html>
```